Simple, elegant, business card design required

Hi designers,I am looking for a simple yet elegant business card design.

Please make use of my logo (attached); you are free to tweak the logo should you wish to do so.

Our business is involved in many different fields - almost all of them involved in some form of "design", so that's really one of the key things I want to portray. I do not wish to specify which field of design, exactly.

I prefer white on black (or just monochromatic), but if you have a different, creative idea, I am open to that too.

You can use artsy photographs provided that you have the license to use those. Please feel free to ask me any questions.
Updates

Project Deadline Extended Reason: Small extension for potential revisions. Did not get the time to provide as much feedback as I can. Added Wednesday, July 09, 2014

Target Market(s)

High-end customers looking for design consultancy

Industry/Entity Type

Business

Contact Information for Business Card

Name: Gareth Moonfield
Position: Creative Director
Mobile: +155603928174
Address: Barrow Lane, Stratford upon Avon, Warwickshire GL12 4RT
Website: torvakest.com (not launched yet)

Requirements
Must have
• Design layout must be clean, original, and text must be readable when printed.
Should not have
• ~ No business card templates please. Anyone using this will be reported.
• ~ Please don't spam entries.

```html
<!DOCTYPE html>
<html lang="en">
<head>
<meta charset="utf-8">
<title>Torvakest Business Card</title>
<link href="https://fonts.googleapis.com/css2?family=Open+Sans:wght@400;600;700&display=swap" rel="stylesheet">
<style>
  :root {
    --stage: #d9d6d3;
    --card: #ffffff;
    --ink: #1f1d1d;
    --block: #272525;
    --muted: #7b7b7b;
    --silver-light: #f2f2f2;
    --silver-dark: #9a9a9a;
    --band: #141414;
  }
  * { box-sizing: border-box; margin: 0; padding: 0; }
  html, body {
    width: 1200px;
    height: 800px;
    overflow: hidden;
    background: var(--stage);
    font-family: "Open Sans", Arial, sans-serif;
    color: var(--ink);
  }
  .card {
    position: absolute;
    left: 180px;
    top: 160px;
    width: 840px;
    height: 480px;
    background: var(--card);
    overflow: hidden;
    box-shadow: 0 10px 30px rgba(0,0,0,0.18);
  }
  .brand-block {
    position: absolute;
    left: 50px;
    top: 80px;
    width: 240px;
    height: 140px;
    background: var(--block);
  }
  .brand-name {
    position: absolute;
    left: 320px;
    top: 88px;
    font-size: 30px;
    font-weight: 400;
    letter-spacing: 9px;
    line-height: 40px;
    color: var(--ink);
  }
  .person {
    position: absolute;
    left: 86px;
    top: 240px;
  }
  .person-name {
    font-size: 22px;
    font-weight: 700;
    line-height: 28px;
  }
  .person-role {
    font-size: 15px;
    line-height: 20px;
    color: var(--muted);
  }
  .contacts {
    position: absolute;
    left: 86px;
    top: 306px;
    list-style: none;
    font-size: 18px;
    line-height: 26px;
  }
  .contacts li {
    display: flex;
    align-items: flex-start;
    gap: 8px;
  }
  .contacts .icon {
    width: 18px;
    height: 18px;
    margin-top: 4px;
    flex: none;
  }
  .contacts .indent { padding-left: 26px; }
  .silver-edge {
    position: absolute;
    left: 0;
    bottom: 38px;
    width: 100%;
    height: 8px;
    background: linear-gradient(180deg, var(--silver-light), var(--silver-dark));
  }
  .base-band {
    position: absolute;
    left: 0;
    bottom: 0;
    width: 100%;
    height: 38px;
    background: var(--band);
  }
</style>
</head>
<body>
  <div class="card">
    <div class="brand-block"></div>
    <div class="brand-name">TORVAKEST</div>

    <div class="person">
      <div class="person-name">Gareth Moonfield</div>
      <div class="person-role">Creative Director</div>
    </div>

    <ul class="contacts">
      <li>
        <svg class="icon" viewBox="0 0 18 18" aria-hidden="true">
          <rect width="18" height="18" fill="#272525"/>
          <rect x="5" y="3" width="8" height="12" rx="1" fill="none" stroke="#fff" stroke-width="1.4"/>
          <rect x="6.8" y="5" width="4.4" height="3" fill="#fff"/>
        </svg>
        <span>+155603928174</span>
      </li>
      <li>
        <svg class="icon" viewBox="0 0 18 18" aria-hidden="true">
          <rect width="18" height="18" fill="#272525"/>
          <path d="M3 9 L9 3.5 L15 9 M5 8 V14.5 H13 V8" fill="none" stroke="#fff" stroke-width="1.5"/>
          <rect x="8" y="10.5" width="2" height="4" fill="#fff"/>
        </svg>
        <span>Barrow Lane, Stratford upon Avon</span>
      </li>
      <li class="indent">Warwickshire GL12 4RT</li>
      <li>
        <svg class="icon" viewBox="0 0 18 18" aria-hidden="true">
          <rect width="18" height="18" fill="#272525"/>
          <circle cx="9" cy="9" r="5.5" fill="none" stroke="#fff" stroke-width="1.2"/>
          <ellipse cx="9" cy="9" rx="2.4" ry="5.5" fill="none" stroke="#fff" stroke-width="1"/>
          <path d="M3.5 9 H14.5" stroke="#fff" stroke-width="1"/>
        </svg>
        <span>torvakest.com</span>
      </li>
    </ul>

    <div class="silver-edge"></div>
    <div class="base-band"></div>
  </div>
</body>
</html>
```